Flyer-Design Immobilienmaklerin Tippgeber Provision
Vielen Dank für das ausgezeichnete Flyer-Design! Selma ist eine sehr freundliche und kompetente Web-Designerin. Die Zusammenarbeit war sehr angenehm! Ich kann Sie wärmstes empfehlen und werde bei Bedarf definitiv wieder auf sie zukommen!
Zielgruppe
www.belvoro-immobilien.de (noch nicht ganz fertig)
Hallo, wir sind Immobilienmaklerinnen die noch nicht ganz so lange dabei sind und noch etwas Unterstützung im Bereich Marketing benötigen. Aus diesem Grund möchten wir einen hochwertigen Flyer designen lassen, welches zu uns widerspiegelt und gleichzeitig unsere Zielgruppe (Immobilienbesitzer) anspricht.
Wir sind offen für alle Vorschläge.
Vielen Dank & LG
Marle
BELVORO Immobilien
Aufgabenstellung
- Format: Flyer DIN lang: 105 x 210 mm (QUER)
- Farben: siehe Webseite www.belvoro-immobilien.de
- Das Design sollte professionell, modern und ansprechend sein, nicht zu viel schnick schnack
- QR Code von der Webseite integrieren
- Wir benötigen eine änderbare Datei um ggf. Texte oder Bilder anzupassen im Nachhinein
- Bildmaterial beigefügt, weitere Bilder von Häusern etc. bitte selbst recherchieren
TEXTE:
Tippgeber Provision
UNSER DANKESCHÖN AN SIE
Sie kennen jemanden, der seine Immobilie verkaufen oder vermieten möchte?
Dann geben Sie uns diesen Tipp weiter und erhalten dafür 10% Tippgeber Provision aus unserer verdienten Brutto-Provision.
Der Ablauf ist wie folgt:
1. Tipp & Kontakt
Sie erfahren von einem geplanten Immobilien-Verkauf (z.B. in Ihrer Nachbarschaft oder bei Freunden) und stellen uns den Kontakt zu den Eigentümern her
2. Vertrag
Wir schließen mit dem Immobilien-Eigentümer einen Maklervertrag
3. Erfolgreiche Vermittlung
Die Immobilie wird von uns erfolgreich vermittelt
4. Tippgeber-Provision
Sobald wir für die erfolgreiche Vermittlung unser Honorar erhalten haben, reichen wir Ihnen Ihre Tippgeber Provision in Höhe von 10% weiter
(in klein)
Voraussetzungen:
Die Immobilie ist uns bisher unbekannt
Die Immobilie wurde noch nicht öffentlich zum Verkauf ausgeschrieben (z.B. in Zeitungen, Internetportale, durch Verkaufsschilder etc.)
Die Immobilie befindet sich im Großraum Hannover
Ihre Immobilienexpertinnen,
Berit Olsenka & Marlene Voskowitz
info@belvoro-immobilien.de
www.belvoro-immobilien.de
INFOS ZUM UNTERNEHMEN:
Über uns
Wir sind ein junges dynamisches Gespann, welches voll und ganz auf die Wünsche und Bedürfnisse unserer Kunden eingeht. Gemeinsam mit Ihnen holen wir das Bestmögliche aus Ihrer Immobilie raus. Wir arbeiten stets wertorientiert und kultur..

```html
<!DOCTYPE html>
<html lang="de">
<head>
<meta charset="utf-8">
<title>BELVORO Immobilien – Tippgeber Provision Flyer</title>
<link href="https://fonts.googleapis.com/css2?family=Crimson+Pro:wght@300;400&family=Montserrat:wght@300;400;500;600&display=swap" rel="stylesheet">
<style>
:root{
  --copper:#c98a66;
  --copper-light:#d9a486;
  --ink:#555558;
  --text:#4a4a4c;
  --dark:#231f20;
  --paper:#ffffff;
  --stage:#e8e8e8;
  --grey-pill:#6b6b6d;
}
*{margin:0;padding:0;box-sizing:border-box}
html,body{width:1200px;height:2400px;overflow:hidden;background:var(--stage)}
body{position:relative;font-family:"Montserrat",sans-serif;color:var(--text)}
.serif{font-family:"Crimson Pro",serif}
.flyer{position:absolute;left:80px;width:1040px;height:520px;background:var(--paper);overflow:hidden;box-shadow:0 4px 14px rgba(0,0,0,.18)}
.flyer--front{top:560px}
.flyer--back{top:1240px}

/* front */
.copper-panel{position:absolute;inset:0;background:var(--copper);clip-path:polygon(832px 0,1040px 0,1040px 520px,520px 520px)}
.portrait-area{position:absolute;left:560px;top:170px;width:480px;height:350px;
  background:linear-gradient(90deg,#e9ddd2 0%,#d8c4b2 40%,#3a302c 62%,#c9b29a 80%,#b99a7f 100%);
  clip-path:polygon(200px 0,480px 0,480px 350px,60px 350px,130px 200px)}
.brand{position:absolute;right:0;top:58px;width:250px;text-align:center;color:#fff}
.brand__name{font-family:"Crimson Pro",serif;font-size:46px;font-weight:400;letter-spacing:2px;line-height:1}
.brand__sub{font-family:"Crimson Pro",serif;font-size:14px;letter-spacing:9px;margin-top:4px}
.headline{position:absolute;left:40px;top:16px;color:var(--ink);font-family:"Crimson Pro",serif;font-weight:400;font-size:60px;line-height:52px;letter-spacing:1px}
.headline__tag{font-family:"Montserrat",sans-serif;font-weight:300;font-size:38px;color:var(--copper);letter-spacing:2px;display:inline-block;border-bottom:1.5px solid var(--copper);padding-bottom:2px;margin-left:10px;vertical-align:6px;line-height:40px}
.question{position:absolute;left:40px;top:140px;width:622px;height:32px;border-radius:10px;background:var(--copper);color:#fff;font-weight:500;font-size:16px;line-height:32px;text-align:center}
.intro{position:absolute;left:40px;top:186px;width:640px;font-size:11.5px;line-height:16px}
.steps{position:absolute;left:40px;top:230px;width:620px}
.step{position:relative;padding-left:58px;margin-bottom:11px}
.step__icon{position:absolute;left:0;top:2px;width:40px;height:36px}
.step__title{font-family:"Crimson Pro",serif;font-size:20px;color:var(--copper);line-height:20px;letter-spacing:.5px}
.step__text{font-size:11px;line-height:16px;margin-top:2px}
.step-line{position:absolute;left:59px;top:275px;height:190px;border-left:1.5px dotted var(--ink)}
.conditions{position:absolute;left:40px;top:454px;width:600px;font-size:6.6px;line-height:9px}
.contact-bar{position:absolute;left:0;bottom:0;width:546px;height:36px;background:var(--dark);color:#fff;font-size:12px;font-weight:500;line-height:36px;padding-left:40px;display:flex;gap:14px;align-items:center}
.contact-bar svg{vertical-align:-2px;margin-right:4px}
.pill-role{position:absolute;left:776px;top:432px;width:264px;height:30px;background:var(--grey-pill);color:#fff;font-size:15px;font-weight:500;line-height:30px;padding-left:14px;border-radius:10px 0 0 10px}
.pill-names{position:absolute;left:740px;top:468px;width:266px;height:30px;background:var(--copper-light);color:#fff;font-size:14.5px;font-weight:500;line-height:30px;text-align:center;border-radius:10px}

/* back */
.back-content{position:absolute;left:30px;top:20px;width:640px}
.section-title{font-family:"Crimson Pro",serif;font-size:17px;color:var(--ink);letter-spacing:.3px;padding-bottom:6px;border-bottom:1px solid var(--copper-light);margin-bottom:14px}
.section-text{font-size:10px;line-height:15px;margin-bottom:9px}
.section-gap{height:6px}
.services{position:absolute;right:0;top:0;width:326px;height:520px;background:var(--dark);padding:28px 0 0 38px;color:#fff}
.service{display:flex;align-items:center;gap:20px;height:51px}
.service svg{flex:0 0 30px}
.service__title{font-family:"Crimson Pro",serif;font-size:14px;line-height:14px;letter-spacing:.4px}
.service__note{font-size:7px;line-height:9px;margin-top:2px}
</style>
</head>
<body>

<section class="flyer flyer--front" aria-label="Flyer Vorderseite">
  <div class="copper-panel"></div>
  <div class="portrait-area" role="img" aria-label="Foto der beiden Immobilienexpertinnen"></div>
  <div class="brand"><div class="brand__name">BELVORO</div><div class="brand__sub">IMMOBILIEN</div></div>

  <h1 class="headline">UNSER DANKESCHÖN<br>AN SIE! <span class="headline__tag">Tippgeber Provision</span></h1>
  <div class="question">Sie kennen jemanden, der seine Immobilie verkaufen oder vermieten möchte?</div>
  <p class="intro">Dann geben Sie uns diesen Tipp weiter und erhalten dafür 10% Tippgeber Provision aus unserer verdienten Brutto-Provision. <b>So funktioniert es:</b></p>

  <div class="step-line"></div>
  <div class="steps">
    <div class="step">
      <svg class="step__icon" viewBox="0 0 40 36"><ellipse cx="16" cy="13" rx="15" ry="11" fill="var(--copper)"/><path d="M6 20 L3 30 L14 23Z" fill="var(--copper)"/><ellipse cx="28" cy="22" rx="11" ry="8" fill="var(--copper-light)"/></svg>
      <div class="step__title">TIPP UND KONTAKT</div>
      <div class="step__text">Sie erfahren von einem geplanten Immobilien-Verkauf (z.B. in Ihrer Nachbarschaft oder bei Freunden) und stellen uns den Kontakt zu den Eigentümern her</div>
    </div>
    <div class="step">
      <svg class="step__icon" viewBox="0 0 40 36"><rect x="8" y="4" width="24" height="30" rx="2" fill="var(--copper)"/><rect x="14" y="1" width="12" height="6" rx="2" fill="var(--copper)"/><path d="M13 14h14M13 20h14M13 26h14" stroke="#fff" stroke-width="2"/></svg>
      <div class="step__title">VERTRAG</div>
      <div class="step__text">Wir schließen mit dem Immobilien-Eigentümer einen Maklervertrag</div>
    </div>
    <div class="step">
      <svg class="step__icon" viewBox="0 0 40 36"><path d="M2 14 L12 8 L20 12 L28 8 L38 14 L30 24 L20 30 L10 24Z" fill="var(--copper)"/><path d="M12 18 L20 24 L28 18" stroke="#fff" stroke-width="2" fill="none"/></svg>
      <div class="step__title">ERFOLGREICHE VERMITTLUNG</div>
      <div class="step__text">Die Immobilie wird von uns erfolgreich vermittelt</div>
    </div>
    <div class="step">
      <svg class="step__icon" viewBox="0 0 40 36"><rect x="6" y="12" width="28" height="22" fill="var(--copper)"/><rect x="4" y="8" width="32" height="7" fill="var(--copper)"/><path d="M20 8v26M4 18h32" stroke="#fff" stroke-width="2"/></svg>
      <div class="step__title">TIPPGEBER-PROVISION</div>
      <div class="step__text">Sobald wir für die erfolgreiche Vermittlung unser Honorar erhalten haben, reichen wir<br>Ihnen Ihre Tippgeber Provision in Höhe von 10% weiter</div>
    </div>
  </div>
  <p class="conditions">Voraussetzungen: Die Immobilie ist uns bisher unbekannt. Die Immobilie wurde noch nicht öffentlich zum Verkauf ausgeschrieben<br>(z.B. in Zeitungen, Internetportale, durch Verkaufsschilder etc.). Die Immobilie befindet sich im Großraum Hannover</p>

  <div class="contact-bar">
    <span><svg width="12" height="9" viewBox="0 0 12 9"><rect width="12" height="9" fill="#fff"/><path d="M0 0 L6 5 L12 0" stroke="var(--dark)" fill="none"/></svg>info@belvoro-immobilien.de</span>
    <span><svg width="11" height="11" viewBox="0 0 11 11"><path d="M2 0 L4 0 L5 3 L3.5 4.5 Q5 7 6.5 7.5 L8 6 L11 7 L11 9 Q9 11 6 9.5 Q2 7.5 0.5 4 Q0 2 2 0Z" fill="#fff"/></svg>0511 48293017</span>
    <span><svg width="11" height="11" viewBox="0 0 11 11"><circle cx="5.5" cy="5.5" r="4.8" stroke="#fff" fill="none"/><path d="M0.7 5.5h9.6M5.5 0.7v9.6" stroke="#fff"/><ellipse cx="5.5" cy="5.5" rx="2.2" ry="4.8" stroke="#fff" fill="none"/></svg>www.belvoro-immobilien.de</span>
  </div>

  <div class="pill-role">Ihre Immobilienexpertinnen</div>
  <div class="pill-names">Berit Olsenka &amp; Marlene Voskowitz</div>
</section>

<section class="flyer flyer--back" aria-label="Flyer Rückseite">
  <div class="back-content">
    <h2 class="section-title">ÜBER UNS</h2>
    <p class="section-text">Wir sind ein junges dynamisches Gespann, welches voll und ganz auf die Wünsche und Bedürfnisse unserer Kunden eingeht. Gemeinsam mit Ihnen holen wir das Bestmögliche aus Ihrer Immobilie raus. Wir arbeiten stets wertorientiert und kulturoffen und freuen uns auf jede neue Herausforderung.</p>
    <p class="section-text">Das eigene Zuhause soll für unsere Kunden der Rückzugsort und die Wohlfühloase werden. Ob mieten oder kaufen, wir suchen Ihnen diesen speziellen Ort.</p>
    <div class="section-gap"></div>
    <h2 class="section-title">UNSER SERVICE</h2>
    <p class="section-text">Immobilien sind viel mehr als nur Bauwerke aus Stein und Mörtel. Die Immobilien Güter sind eng mit Erinnerungen, Träumen und Gefühlen verbunden. Ihre Bewohner füllen sie mit Leben und geben ihnen Mehrwert. Ihre Makler von BELVORO Immobilien wissen das. Für uns geht es nicht nur um Immobilien, sondern auch um die Menschen dahinter. Deswegen widmen wir uns Immobiliengeschäften ganzheitlich und mit Weitsicht.</p>
    <p class="section-text">Ob Immobilienkauf, Immobilienvermietung oder Immobilienverkauf: Sie als Kunde stehen für uns im Fokus. Ehrlich, seriös und allumfassend beraten wir Sie. Dabei agieren Ihre Anforderungen als Kompass für unser transparentes Handeln. Lernen Sie uns kennen!</p>
    <div class="section-gap"></div>
    <h2 class="section-title">FACHWISSEN TRIFFT AUF ERFAHRUNG UND ENGAGEMENT</h2>
    <p class="section-text">Erfolg in Immobiliengeschäften ist kein Zufall. Fachwissen fusioniert mit Erfahrung und Engagement, um die besten Ergebnisse zu erzielen.</p>
    <p class="section-text">Ihre Makler von BELVORO Immobilien setzen sich für Sie und Ihre Belange ein. Bei uns profitieren Sie von einem professionellen Vorgehen und einer aufrichtigen Leidenschaft für den Job. Unsere Beratung ist bedarfs- und zielorientiert. An einer großen Portion an Feingefühl und Empathie mangelt es nicht. Kontaktieren Sie uns für einen zuverlässigen Immobilienservice in Isernhagen!</p>
  </div>

  <div class="services">
    <div class="service"><svg width="30" height="26" viewBox="0 0 30 26"><path d="M2 13 L15 2 L28 13 H24 V25 H6 V13Z" fill="var(--copper)"/></svg><div class="service__title">VERKAUF UND VERMIETUNG<br>DER IMMOBILIEN</div></div>
    <div class="service"><svg width="30" height="26" viewBox="0 0 30 26"><rect x="7" y="3" width="16" height="22" rx="2" fill="var(--copper)"/><path d="M11 10h8M11 15h8M11 20h8" stroke="var(--dark)" stroke-width="2"/></svg><div class="service__title">KOSTENLOSE<br>WERTERMITTLUNG</div></div>
    <div class="service"><svg width="30" height="26" viewBox="0 0 30 26"><path d="M2 5 Q9 2 14 6 V23 Q9 19 2 22Z M28 5 Q21 2 16 6 V23 Q21 19 28 22Z" fill="var(--copper)"/></svg><div><div class="service__title">ERSTELLUNG EINES EXPOSÉS</div><div class="service__note">inklusive Wohnflächenberechnung, Grundriss-<br>erstellung, Immobilienfotografie</div></div></div>
    <div class="service"><svg width="30" height="26" viewBox="0 0 30 26"><circle cx="15" cy="13" r="11" stroke="var(--copper)" stroke-width="2.5" fill="none"/><path d="M4 13h22M15 2v22" stroke="var(--copper)" stroke-width="2"/><ellipse cx="15" cy="13" rx="5" ry="11" stroke="var(--copper)" stroke-width="2" fill="none"/></svg><div class="service__title">VERÖFFENTLICHUNG DER<br>IMMOBILIE</div></div>
    <div class="service"><svg width="30" height="26" viewBox="0 0 30 26"><circle cx="15" cy="13" r="6" fill="var(--copper)"/><path d="M15 1v5M15 20v5M3 13h5M22 13h5M6.5 4.5l3.5 3.5M20 18l3.5 3.5M23.5 4.5L20 8M10 18l-3.5 3.5" stroke="var(--copper)" stroke-width="2.5"/></svg><div class="service__title">ERSTELLUNG DES<br>ENERGIEAUSWEISES</div></div>
    <div class="service"><svg width="30" height="26" viewBox="0 0 30 26"><path d="M2 13 L15 2 L28 13 H24 V25 H18 V17 H12 V25 H6 V13Z" fill="var(--copper)"/></svg><div class="service__title">HOMESTAGING<br>(VERKAUFSOPTIMIERUNG)</div></div>
    <div class="service"><svg width="30" height="26" viewBox="0 0 30 26"><circle cx="15" cy="8" r="5" fill="var(--copper)"/><circle cx="5" cy="10" r="3.5" fill="var(--copper)"/><circle cx="25" cy="10" r="3.5" fill="var(--copper)"/><path d="M6 24 Q6 15 15 15 Q24 15 24 24Z M0 22 Q0 15 6 15 L5 22Z M30 22 Q30 15 24 15 L25 22Z" fill="var(--copper)"/></svg><div class="service__title">OPEN-HOUSE<br>BESICHTIGUNGEN</div></div>
    <div class="service"><svg width="30" height="26" viewBox="0 0 30 26"><path d="M2 13 L15 2 L28 13 H24 V25 H6 V13Z" fill="var(--copper)"/><path d="M11 20 L19 12" stroke="var(--dark)" stroke-width="2.5"/></svg><div class="service__title">SANIERUNG VON<br>WOHNRÄUMEN</div></div>
    <div class="service"><svg width="30" height="26" viewBox="0 0 30 26"><path d="M1 11 L9 5 L15 9 L21 5 L29 11 L22 19 L15 24 L8 19Z" fill="var(--copper)"/><path d="M9 14 L15 19 L21 14" stroke="var(--dark)" stroke-width="2" fill="none"/></svg><div><div class="service__title">UMFANGREICHE KONTAKTE</div><div class="service__note">im Bereich Sanierung und Bau, Steuerberater,<br>Anwälte und Finanzierungen</div></div></div>
  </div>
</section>

</body>
</html>
```